Sign Shop website

We need a web design for a sign company called Quillby Signs that builds signs for shops such as A Frames, Banners, Tennet Boards, Shop front windows etc...

The existing site is avaliable at www.quillbysigns.com.au

We will need to have a fresh makeover. The new site must have the following:

Photo Galleries (broken down into sections)
Store Locations (currently there are 4 stores)
Online quote form
List of services
About Us Page

We just need to front page designed in photoshop (the inner page is not necessary) We have a team that can code the site up.

The website should have the exact logo. Any person who alters the logo, design will be elimated.

No Twitter, RSS, LinkedIn icons

The main colours are yellow, black, blue, red

Target Market(s)

Any business

Industry/Entity Type

It Company

Requirements
Must have
• jQuery slider banner
Should not have
• Alter the logo in any way

```html
<!DOCTYPE html>
<html lang="en">
<head>
<meta charset="utf-8">
<title>Quillby Signs</title>
<link href="https://fonts.googleapis.com/css2?family=Open+Sans:ital,wght@0,400;0,600;0,700;1,700;1,800&display=swap" rel="stylesheet">
<style>
:root{
  --plum:#8e3c76;
  --plum-light:#9d4a85;
  --amber:#f0b030;
  --white:#ffffff;
  --ink:#111111;
  --red:#e0441c;
  --tab-grey:#b5b0af;
  --sky:#6fb3f7;
  --sky-pale:#e3eefa;
  --field:#f8f8fc;
  --field-line:#d6dde8;
  --sage:#8a9890;
  --label:#333333;
}
*{box-sizing:border-box;margin:0;padding:0}
html,body{width:1079px;height:1200px;overflow:hidden;background:var(--white)}
body{position:relative;font-family:"Open Sans",Verdana,sans-serif;color:var(--ink)}
.abs{position:absolute}

.masthead{left:0;top:0;width:1079px;height:454px;background:var(--plum)}
.header-bar{left:0;top:28px;width:1079px;height:45px;background:var(--amber)}
.search{left:672px;top:38px;width:309px;height:27px;background:var(--white);border:1px solid #ddd;display:flex;align-items:center;justify-content:space-between;padding:0 8px 0 4px;font-size:10.5px;letter-spacing:.6px}

.slider{left:91px;top:80px;width:897px;height:350px;background:var(--white);border-radius:6px;padding:6px}
.slide{width:100%;height:100%;background:radial-gradient(ellipse at 70% 65%,#3a78e8 0%,#1447b8 35%,#071a50 75%,#020616 100%)}
.brand{left:70px;top:6px;width:345px;height:132px;background:var(--plum);border-bottom-right-radius:60px;border-right:5px solid var(--white);border-bottom:5px solid var(--white);display:flex;align-items:center;gap:10px;padding-left:14px}
.brand-name{font-size:27px;font-weight:700;color:var(--amber);white-space:nowrap}
.brand-dot{width:22px;height:22px;border-radius:50%;background:var(--amber)}
.brand-wrap{left:70px;top:0;width:345px;height:28px;background:var(--plum)}

.slider-nav{left:714px;top:376px;width:254px;height:35px;background:#dcdcdc;border-radius:4px;display:flex;align-items:center;padding-left:16px;gap:8px}
.dot{width:13px;height:13px;border-radius:50%;background:#3a3a3a}
.dot.current{width:19px;height:19px;background:var(--white);border:4px solid #2a8ad8}
.nav-sep{width:1px;height:24px;background:#aaa;margin:0 8px 0 6px}

.tabs{left:96px;top:435px;display:flex;gap:9px}
.tab{width:150px;height:38px;border-radius:10px 10px 0 0;background:var(--tab-grey);font-size:13px;display:flex;align-items:center;justify-content:center;color:#222}
.tab.active{background:var(--plum);color:var(--white);border-radius:0 0 10px 10px}

.welcome{left:100px;top:503px;font-size:20px;font-weight:800;font-style:italic}
.intro{left:99px;top:547px;width:890px;font-size:12.7px;line-height:18.7px}
.intro strong{color:var(--red);font-weight:600}

.gallery-title{left:99px;top:630px;font-size:15px;font-weight:700;font-style:italic;color:#333}
.rule{border-top:1px dashed #c8c8c8}
.thumbs{left:110px;top:687px;display:grid;grid-template-columns:repeat(3,140px);column-gap:15px;row-gap:15px}
.thumb{height:75px;border-radius:10px;background:var(--tab-grey)}

.stores{left:96px;top:912px;width:576px;height:155px;border-radius:3px;overflow:hidden;background:linear-gradient(135deg,#e8dcc8,#d8c8b0 50%,#c8b89a)}
.stores-panel{left:0;top:0;width:340px;height:155px;background:var(--sage);border-radius:0 140px 140px 0 / 0 90px 90px 0;box-shadow:12px 0 0 var(--white)}
.stores-title{left:28px;top:16px;font-size:26px;font-weight:800;font-style:italic;color:#2f3a36}
.stores-sub{left:28px;top:51px;font-size:12px;font-weight:700;font-style:italic;color:var(--white)}
.postcode{left:28px;top:100px;width:307px;height:27px;background:var(--white);display:flex;align-items:center;justify-content:space-between;padding:0 4px 0 14px;font-size:11px;font-weight:700;font-style:italic;color:#555}

.quote{left:690px;top:606px;width:314px;height:513px;background:var(--sky-pale)}
.quote-head{left:0;top:0;width:314px;height:47px;background:var(--sky);display:flex;align-items:center;justify-content:flex-end;padding-right:30px;font-size:23px;font-weight:800;font-style:italic;color:var(--white)}
.fields{left:17px;top:66px;width:278px}
.field{display:flex;justify-content:space-between;align-items:center;height:28px;font-size:12px;color:var(--label)}
.field span.input{width:165px;height:20px;background:var(--field);border:1px solid var(--field-line)}
.other-label{left:17px;top:354px;font-size:12px;color:var(--label)}
.other{left:17px;top:378px;width:278px;height:83px;background:var(--field);border:1px solid var(--field-line)}
.submit{left:196px;top:473px;width:97px;height:31px;background:var(--sky);color:var(--white);font-size:18px;display:flex;align-items:center;justify-content:center}

.footer{left:0;top:1119px;width:1079px;height:81px;background:var(--plum);overflow:hidden}
.footer-wave{left:-100px;top:44px;width:1279px;height:120px;border-radius:50%;background:var(--plum-light)}
.footer-link{top:32px;font-size:13px;color:var(--white)}
.copyright{left:0;top:61px;width:1079px;text-align:center;font-size:10px;color:#d7b9cf}
</style>
</head>
<body>
<div class="abs masthead"></div>
<div class="abs header-bar"></div>

<div class="abs search">Search Catalogues
  <svg width="22" height="22" viewBox="0 0 22 22"><circle cx="11" cy="11" r="10" fill="#a9a9a9"/><circle cx="10" cy="10" r="4.5" fill="none" stroke="#fff" stroke-width="2"/><line x1="13" y1="13" x2="17" y2="17" stroke="#fff" stroke-width="2.5"/></svg>
</div>

<div class="abs slider"><div class="slide" role="img" aria-label="Close-up of a large-format digital printer in blue light"></div></div>

<div class="abs brand-wrap"></div>
<div class="abs brand"><span class="brand-dot"></span><span class="brand-name">Quillby Signs</span></div>

<div class="abs slider-nav">
  <span class="dot"></span><span class="dot"></span><span class="dot"></span><span class="dot"></span><span class="dot"></span><span class="dot"></span><span class="dot current"></span>
  <span class="nav-sep"></span>
  <svg width="60" height="20" viewBox="0 0 60 20"><path d="M14 3 L6 10 L14 17" fill="none" stroke="#333" stroke-width="3"/><path d="M44 3 L52 10 L44 17" fill="none" stroke="#333" stroke-width="3"/></svg>
</div>

<nav class="abs tabs">
  <div class="tab active">About Us</div>
  <div class="tab">Our Services</div>
  <div class="tab">OurPortfolio</div>
  <div class="tab">Contact Us</div>
</nav>

<h1 class="abs welcome">Welcome</h1>
<p class="abs intro"><strong>Quillby Signs</strong> is a West Australian owned and managed company. We manufacture signage for any application; vinyl lettering, pull up banners, vehicle signage, in fact anything that requires our customers seeing the full picture when it comes to advertising their business. So if you're serious about the best, put us to the test!</p>

<h2 class="abs gallery-title">Photo Gallery</h2>
<div class="abs rule" style="left:96px;top:653px;width:592px"></div>
<div class="abs thumbs">
  <div class="thumb"></div><div class="thumb"></div><div class="thumb"></div>
  <div class="thumb"></div><div class="thumb"></div><div class="thumb"></div>
</div>
<div class="abs rule" style="left:110px;top:871px;width:578px"></div>

<section class="abs stores" role="img" aria-label="Road map with a red pin marking a store location">
  <div class="abs stores-panel"></div>
  <div class="abs stores-title">Store Locations</div>
  <div class="abs stores-sub">Find a Quillby&nbsp; Store Near You</div>
  <div class="abs postcode">Enter your postcode
    <svg width="22" height="22" viewBox="0 0 22 22"><circle cx="11" cy="11" r="10" fill="#a9a9a9"/><circle cx="10" cy="10" r="4.5" fill="none" stroke="#fff" stroke-width="2"/><line x1="13" y1="13" x2="17" y2="17" stroke="#fff" stroke-width="2.5"/></svg>
  </div>
</section>

<section class="abs quote">
  <div class="abs quote-head">
    <svg class="abs" style="left:22px;top:4px" width="44" height="42" viewBox="0 0 44 42"><path d="M4 6 L8 2 L38 32 L40 40 L32 38 Z" fill="#3a78c8"/></svg>
    Request a Quote
  </div>
  <div class="abs fields">
    <div class="field">Name:<span class="input"></span></div>
    <div class="field">Company:<span class="input"></span></div>
    <div class="field">Phone:<span class="input"></span></div>
    <div class="field">Email Address:<span class="input"></span></div>
    <div class="field">Suburb:<span class="input"></span></div>
    <div class="field">Store:<span class="input"></span></div>
    <div class="field">Sign Type:<span class="input"></span></div>
    <div class="field">Material:<span class="input"></span></div>
    <div class="field">Sign Size:<span class="input"></span></div>
    <div class="field">Artwork Required:<span class="input"></span></div>
  </div>
  <div class="abs other-label">Other Information</div>
  <div class="abs other"></div>
  <div class="abs submit">Submit</div>
</section>

<footer class="abs footer">
  <div class="abs footer-wave"></div>
  <span class="abs footer-link" style="left:283px">About Us</span>
  <span class="abs footer-link" style="left:427px">Our Services</span>
  <span class="abs footer-link" style="left:590px">OurPortfolio</span>
  <span class="abs footer-link" style="left:752px">Contact Us</span>
  <div class="abs copyright">© 2013 Quillby Signs</div>
</footer>
</body>
</html>
```